I have written a young adult novel called "Brisa". It's about a unique young 16 year old girl who becomes a Helper, in conjunction with a Sprite called Tovi. She is based in Zambia in Africa. I plan to publish the book on-line and need a great cover. The cover will be seen in full and also as a thumbnail. Synopsis attached - target market would be young females aged from about 10 - 16.
Updates

thanks for all your efforts so far.  Thought I should clarify that Brisa is a 16 year old European living in Africa so she is not actually African.  Can I also ask that you please submit a thumbnail size image of the cover as well so I can see what it would look like on Pellow.  Can you please use just my initials for author name - M.J Fenwick (not Glenda).  Thanks! 

Reason: feel that you have all provided some great work but I need a little bit more time to decide on exactly what my focus needs to be in terms of target audience - I was thinking females aged about 10 to 16 but may be that I should allow myself to target a wider audience, to include older females especially but also some males. The other strong character in the book is a young man called Ned. It is Brisa's task as a Helper to lead Ned to safety so he features in alternating chapters until their paths cross when she rescues him ... So I would like a bit more time to decide whether to go with quite a feminine design or something a little less targeted ... So thanks for all your hard work - getting there ,,, I will give more feedback this week to you individually.

Industry/Entity Type

Adult

Requirements
Must have
• the title of the book - Brisa, and my name as author
Should not have
• Don't want just a picture of the girl Brisa - perhaps more of a silhouette or line representation of her as she needs to exist in the reader's imagination

```html
<!DOCTYPE html>
<html lang="en">
<head>
<meta charset="utf-8">
<title>Brisa – Book Cover</title>
<link rel="stylesheet" href="https://fonts.googleapis.com/css2?family=Arimo:wght@400;700&family=Cinzel:wght@400&family=Lato:wght@400&display=swap">
<style>
  :root {
    --page: #ffffff;
    --ink-dark: #000000;
    --ink-light: #ffffff;
    --sky-top: #2d5a8a;
    --sky-mid: #6f9bc6;
    --sky-haze: #c8d5dc;
    --dusk-glow: #e59b3a;
    --ground: #0a0604;
  }
  * { margin: 0; padding: 0; box-sizing: border-box; }
  html, body {
    width: 1200px; height: 1000px; overflow: hidden;
    background: var(--page);
  }
  .canvas { position: relative; width: 1200px; height: 1000px; }

  .cover-wrap {
    position: absolute; left: 89px; top: 145px;
    width: 1025px; height: 717px;
  }

  .back-cover {
    position: absolute; left: 0; top: 0;
    width: 475px; height: 717px;
    background: var(--ink-dark);
    color: var(--ink-light);
  }
  .synopsis {
    position: absolute; left: 35px; top: 38px; width: 409px;
    font-family: "Arimo", Arial, sans-serif;
    font-weight: 700; font-size: 10.6px; line-height: 15.1px;
    text-align: justify; hyphens: manual;
  }
  .signature {
    position: absolute; left: 35px; top: 670px;
    font-family: "Arimo", Arial, sans-serif;
    font-size: 17px; font-weight: 400;
  }

  .front-cover {
    position: absolute; left: 475px; top: 0;
    width: 550px; height: 717px;
    overflow: hidden;
  }
  .cover-photo {
    position: absolute; inset: 0;
    background: linear-gradient(180deg,
      var(--sky-top) 0%,
      var(--sky-mid) 32%,
      var(--sky-haze) 62%,
      #d9c9a6 76%,
      var(--dusk-glow) 82%,
      var(--ground) 87%,
      var(--ink-dark) 100%);
  }
  .title {
    position: absolute; left: 75px; right: 0; top: 28px;
    text-align: center;
    font-family: "Cinzel", "Times New Roman", serif;
    font-size: 72px; font-weight: 400; letter-spacing: 2px;
    color: var(--ink-light);
  }
  .author {
    position: absolute; left: 75px; right: 0; top: 666px;
    text-align: center;
    font-family: "Lato", Arial, sans-serif;
    font-size: 18px; color: var(--ink-light);
  }

  .spine-title, .spine-author {
    position: absolute; color: var(--ink-light);
    writing-mode: vertical-rl; white-space: nowrap;
  }
  .spine-title {
    left: 16px; top: 44px;
    font-family: "Cinzel", "Times New Roman", serif;
    font-size: 40px; letter-spacing: 3px; line-height: 1;
  }
  .spine-author {
    left: 19px; top: 614px;
    font-family: "Lato", Arial, sans-serif;
    font-size: 14px; line-height: 1;
  }
</style>
</head>
<body>
<div class="canvas">
  <div class="cover-wrap">
    <section class="back-cover">
      <div class="synopsis">
        <p>Brisa is a one-of-a-kind girl of sixteen, raised in Zambia, Africa, in a warm and happy home with her mother Maren. Her world falls apart when Maren becomes gravely ill, and in spite of every effort to heal her, Maren is lost.</p>
        <p>Brisa's sorrow runs so deep that her aura blazes with a light bright enough to reach Tovi, the Sprite, who hurries to be by her side. Through long talks under the stars Tovi helps Brisa begin to mend her broken heart, and shows her how to draw in The Energy along with other gifts she will need for the road that lies ahead of her.</p>
        <p>Brisa learns that she is meant to walk the same path her mother once walked and become a Helper. Her first task takes her across the border, where she must find and free Ned Kanda, son of Elias, who leads a band of rebels. The rebels are gathering their strength to stand against a cruel and ruthless regime.</p>
        <p>Tovi goes with Brisa as her guide and lookout. The two can speak mind to mind, so Tovi can warn her of danger and help her think her way through each new trouble they meet. Brisa can also call on The Field to push back threats and shape things from thin air to throw off anyone who follows them on the road.</p>
        <p>In alternating chapters we follow Brisa and meet Ned and his friend Jonah, who are seized by the cold-hearted Sergeant Voss, who plans to trade Ned for his father. Brisa reaches them in time, sets them free and sets out to guide them across the wild country to safety.</p>
      </div>
      <p class="signature">Glenda Fenwick, October 2013</p>
    </section>

    <section class="front-cover">
      <div class="cover-photo" role="img" aria-label="Dusk sky fading from blue to an orange horizon, with silhouettes of two girls sitting back to back in tall grass"></div>
      <h1 class="title">BRISA</h1>
      <p class="author">M.J Fenwick</p>
      <span class="spine-title">BRISA</span>
      <span class="spine-author">M.J Fenwick</span>
    </section>
  </div>
</div>
</body>
</html>
```